Beautiful Quotes For Social Media Posts

We are looking for 5 beautifully designed quotes for our social media account.

Inspiration of styles we like in both style and color along with a few of our favorite fonts (you are NOT limited to these fonts this is just to give you an idea):
https://quillmorestudio.example.com/s/k7p2vx9tqa41mzn8wbd3ce6hr5lf0y2j

*These fonts are property of Quillmore Studio. You do not have permission/rights to use them outside of this assignment*

Quotes to use (5):
“Only those who dare to fail greatly can ever achieve greatly.” –Vernon T. Ashgrove
“Don’t go through life, grow through life.” – Milo Pendrake
“Follow your bliss and the universe will open doors where there were only walls.” – Arthur Venholm
“If you don’t like the road you’re walking, start paving another one.” – Greta Mossley
“Life is like riding a bicycle. To keep your balance, you must keep moving.” —Lucian Thornwick

File Specifics:
- JPG
- 10x10 in size (square)
- Please include @QuillmoreStudio in the bottom right left or center of each design

Brand Details:
Soft but rich pastel and bright colors.
Hand Drawn florals, doodles and art
Handwritten looking fonts
Artsy, Creative, Girl and Inspiring

```html
<!DOCTYPE html>
<html lang="en">
<head>
<meta charset="utf-8">
<title>Follow Your Bliss – Quote Post</title>
<link rel="stylesheet" href="https://fonts.googleapis.com/css2?family=Amatic+SC:wght@700&family=Fredoka:wght@600&family=Mrs+Saint+Delafield&family=Nunito:wght@600&display=swap">
<style>
  :root {
    --stripe: #e1e6f8;
    --paper: #ffffff;
    --plum: #75709a;
    --ink-light: #ffffff;
    --universe: #dfe3f8;
    --signature: #111111;
  }
  html, body {
    margin: 0;
    padding: 0;
    overflow: hidden;
  }
  .post {
    position: relative;
    width: 1200px;
    height: 1200px;
    overflow: hidden;
    background: repeating-linear-gradient(45deg, var(--stripe) 0 70px, var(--paper) 70px 200px);
  }
  .card-frame {
    position: absolute;
    left: 404px;
    top: 62px;
    width: 391px;
    height: 1074px;
    box-sizing: border-box;
    background: var(--paper);
    border: 4px solid var(--plum);
  }
  .quote-panel {
    position: absolute;
    left: 428px;
    top: 90px;
    width: 345px;
    height: 1020px;
    background: var(--plum);
  }
  .quote {
    position: absolute;
    left: 0;
    top: 9px;
    width: 100%;
    margin: 0;
    display: flex;
    flex-direction: column;
    align-items: center;
    text-align: center;
  }
  .quote-line {
    display: block;
    height: 70px;
    line-height: 70px;
    font-family: "Amatic SC", cursive;
    font-weight: 700;
    font-size: 74px;
    color: var(--ink-light);
    letter-spacing: 1px;
  }
  .quote-highlight {
    display: block;
    height: 92px;
    line-height: 92px;
    font-family: "Fredoka", sans-serif;
    font-weight: 600;
    font-size: 84px;
    color: var(--universe);
    letter-spacing: 1px;
  }
  .sparkles {
    position: absolute;
    left: 0;
    top: 0;
    width: 1200px;
    height: 1200px;
    pointer-events: none;
  }
  .sparkles .spark { fill: var(--universe); }
  .attribution {
    position: absolute;
    right: 406px;
    top: 1108px;
    padding: 0 6px;
    background: var(--paper);
    font-family: "Mrs Saint Delafield", cursive;
    font-size: 40px;
    line-height: 56px;
    color: var(--signature);
    white-space: nowrap;
  }
  .handle {
    position: absolute;
    left: 108px;
    top: 1164px;
    padding: 0 3px;
    border-left: 2px solid var(--plum);
    border-right: 2px solid var(--plum);
    border-bottom: 2px solid var(--plum);
    font-family: "Nunito", sans-serif;
    font-weight: 600;
    font-size: 17px;
    line-height: 20px;
    color: var(--plum);
  }
</style>
</head>
<body>
<main class="post">
  <div class="card-frame"></div>
  <section class="quote-panel">
    <p class="quote">
      <span class="quote-line">Follow</span>
      <span class="quote-line">Your</span>
      <span class="quote-line">Bliss</span>
      <span class="quote-line">And</span>
      <span class="quote-line">The</span>
      <span class="quote-highlight">universe</span>
      <span class="quote-line">Will</span>
      <span class="quote-line">Open</span>
      <span class="quote-line">Doors</span>
      <span class="quote-line">Where</span>
      <span class="quote-line">There</span>
      <span class="quote-line">Were</span>
      <span class="quote-line">Only</span>
      <span class="quote-line">Walls</span>
    </p>
  </section>
  <svg class="sparkles" viewBox="0 0 1200 1200" aria-hidden="true">
    <circle class="spark" cx="494" cy="392" r="5"/>
    <circle class="spark" cx="754" cy="434" r="5"/>
    <circle class="spark" cx="520" cy="550" r="5"/>
    <circle class="spark" cx="672" cy="554" r="5"/>
    <circle class="spark" cx="502" cy="586" r="5"/>
    <circle class="spark" cx="702" cy="584" r="5"/>
    <path class="spark" d="M466 418 l5 10 11 2 -8 8 2 11 -10 -5 -10 5 2 -11 -8 -8 11 -2z"/>
    <path class="spark" d="M676 404 q2 14 16 16 q-14 2 -16 16 q-2 -14 -16 -16 q14 -2 16 -16z"/>
    <path class="spark" d="M468 544 q2 12 14 14 q-12 2 -14 14 q-2 -12 -14 -14 q12 -2 14 -14z"/>
    <path class="spark" d="M724 542 l4 9 10 1 -7 7 2 10 -9 -5 -9 5 2 -10 -7 -7 10 -1z"/>
  </svg>
  <p class="attribution">Arthur Venholm</p>
  <p class="handle">@QuillmoreStudio</p>
</main>
</body>
</html>
```